Ember Fold Whiskey Label

We are looking for a label to be made for our single batch whiskey. in the attached pdf you will see the lay out of the design. We are going to use a whiskey bottle with a cork. Some of the label you will need to leave some space for hand writing.

Target Market(s)

people who like craft beer and whiskey

Industry/Entity Type

Craft Distillery

Font styles to use
Decorative

Colors

Designer to choose colors to be used in the design.

Requirements
Must have
• room for hand writing informatiom

```html
<!DOCTYPE html>
<html lang="en">
<head>
<meta charset="utf-8">
<title>Ember Fold Whiskey Label</title>
<link rel="stylesheet" href="https://fonts.googleapis.com/css2?family=Rye&family=Josefin+Sans:wght@600;700&display=swap">
<style>
  :root {
    --bg: #d8dcde;
    --paper: #f9fafa;
    --gold: #e2c12a;
    --gold-deep: #b8860b;
    --ink: #1f2326;
    --shadow: rgba(0,0,0,0.18);
  }
  * { margin: 0; padding: 0; box-sizing: border-box; }
  html, body { width: 1200px; height: 1200px; overflow: hidden; background: var(--bg); }
  .canvas { position: relative; width: 1200px; height: 1200px; }
  .label { position: absolute; left: 290px; top: 145px; width: 620px; height: 910px; }
  .label-shape { position: absolute; inset: 0; overflow: visible; filter: drop-shadow(0 6px 10px var(--shadow)); }
  .ornament {
    position: absolute;
    background: linear-gradient(135deg, #f3d768, var(--gold-deep));
    border-radius: 40% 60% 50% 50%;
    opacity: 0.85;
  }
  .brand-name {
    position: absolute; left: 0; right: 0; top: 112px;
    text-align: center; font-family: "Rye", serif; font-size: 60px;
    color: var(--ink); letter-spacing: 1px; line-height: 1;
  }
  .brand-sub {
    position: absolute; left: 0; right: 0; top: 190px;
    text-align: center; font-family: "Rye", serif; font-size: 48px;
    color: var(--ink); line-height: 1;
  }
  .product-name {
    position: absolute; left: 150px; right: 150px; top: 260px; height: 40px;
    border-top: 2px solid var(--gold); border-bottom: 2px solid var(--gold);
    text-align: center; font-family: "Josefin Sans", sans-serif; font-weight: 600;
    font-size: 23px; letter-spacing: 2px; color: var(--ink); line-height: 40px;
  }
  .tagline {
    position: absolute; left: 0; right: 0; top: 320px;
    text-align: center; font-family: "Josefin Sans", sans-serif; font-weight: 600;
    font-size: 18px; letter-spacing: 1.5px; color: var(--ink);
  }
  .rule { position: absolute; left: 70px; right: 70px; height: 2px; background: var(--gold); }
  .rule::before, .rule::after {
    content: ""; position: absolute; top: -5px; width: 10px; height: 10px;
    border: 2px solid var(--gold-deep); border-radius: 50%;
  }
  .rule::before { left: -12px; }
  .rule::after { right: -12px; }
  .field {
    position: absolute; border: 2.5px solid var(--gold); border-radius: 10px;
    padding: 5px 7px; font-family: "Josefin Sans", sans-serif; font-weight: 700;
    font-size: 13px; letter-spacing: 0.5px; color: var(--ink);
  }
  .footer {
    position: absolute; left: 0; right: 0; top: 768px;
    text-align: center; font-family: "Josefin Sans", sans-serif; font-weight: 700;
    font-size: 19px; letter-spacing: 1.5px; line-height: 20px; color: var(--ink);
  }
  .volume {
    position: absolute; left: 0; right: 0; top: 842px;
    text-align: center; font-family: "Josefin Sans", sans-serif; font-weight: 600;
    font-size: 22px; letter-spacing: 1.5px; color: var(--ink);
  }
  .volume-rule { position: absolute; top: 856px; height: 2px; width: 150px; background: var(--gold); }
</style>
</head>
<body>
<div class="canvas">
  <div class="label">
    <svg class="label-shape" viewBox="0 0 620 910" width="620" height="910">
      <path fill="#ffffff" d="M0,110 Q0,80 30,78 L120,78 Q200,0 310,0 Q420,0 500,78 L590,78 Q620,80 620,110 L620,860 Q620,910 570,910 L50,910 Q0,910 0,860 Z"/>
      <path fill="var(--gold)" d="M8,112 Q8,88 34,86 L124,86 Q204,8 310,8 Q416,8 496,86 L586,86 Q612,88 612,112 L612,858 Q612,902 568,902 L52,902 Q8,902 8,858 Z"/>
      <path fill="var(--paper)" d="M20,118 Q20,98 42,97 L130,97 Q208,21 310,21 Q412,21 490,97 L578,97 Q600,98 600,118 L600,852 Q600,890 562,890 L58,890 Q20,890 20,852 Z"/>
      <path fill="none" stroke="var(--ink)" stroke-width="3.5" stroke-linecap="round" stroke-dasharray="0 7" d="M32,124 Q32,110 48,109 L136,109 Q212,34 310,34 Q408,34 484,109 L572,109 Q588,110 588,124 L588,846 Q588,878 556,878 L64,878 Q32,878 32,846 Z"/>
    </svg>

    <div class="ornament" role="img" aria-label="Gold scroll flourish" style="left:160px;top:80px;width:80px;height:26px;"></div>
    <div class="ornament" role="img" aria-label="Gold scroll flourish" style="left:380px;top:80px;width:80px;height:26px;"></div>
    <div class="ornament" role="img" aria-label="Gold scroll flourish" style="left:48px;top:185px;width:60px;height:60px;"></div>
    <div class="ornament" role="img" aria-label="Gold scroll flourish" style="left:512px;top:185px;width:60px;height:60px;"></div>

    <div class="brand-name">IRON LANTERN</div>
    <div class="brand-sub">· DISTILLERY ·</div>
    <div class="product-name">· EMBER FOLD ·</div>
    <div class="tagline">SPIRITS FROM MALT MASH AND HOPS</div>
    <div class="rule" style="top:362px;"></div>

    <div class="field" style="left:68px;top:382px;width:484px;height:66px;">DISTILLATE SOURCE:</div>
    <div class="field" style="left:68px;top:462px;width:232px;height:126px;">AGED:</div>
    <div class="field" style="left:320px;top:462px;width:232px;height:126px;">% ACL. BY VOL.</div>
    <div class="field" style="left:68px;top:600px;width:232px;height:126px;">BOTTLE:</div>
    <div class="field" style="left:320px;top:600px;width:232px;height:126px;">OF:</div>

    <div class="rule" style="top:745px;"></div>
    <div class="footer">DISTILLED BOTTLE BY<br>IRON LANTERN DISTILLERY LLC<br>48 CEDAR LANE. HARLOW CREEK NJ 08999</div>
    <div class="volume-rule" style="left:80px;"></div>
    <div class="volume">750 ML.</div>
    <div class="volume-rule" style="right:80px;"></div>
  </div>
</div>
</body>
</html>
```